Professional looking Roller Blind Discount Card that portrays quality at a value for money price!

We need a double sided business card designed as a discount card. Size 90mm wide x 55mm high.We would like it to look professional and portray quality at a value for money price point.I have uploaded a word document with a basic layout with the information we want included on each side of the card. Please put your own thought into the layout.

Contact Information for Business Card

As per word document attached.

```html
<!DOCTYPE html>
<html lang="en">
<head>
<meta charset="utf-8">
<title>Roller Blinds Discount Card</title>
<link rel="stylesheet" href="https://fonts.googleapis.com/css2?family=Open+Sans:wght@400;600;700;800&display=swap">
<style>
  :root {
    --page: #e7e4df;
    --ink: #0b0b0e;
    --ink-soft: #24252b;
    --gold: #d6a537;
    --gold-light: #f6da7e;
    --gold-deep: #8a5a12;
    --blue: #2ea6e6;
    --blue-deep: #0f6fa8;
    --grey: #a9abb0;
  }
  * { box-sizing: border-box; margin: 0; padding: 0; }
  html, body {
    width: 1200px; height: 800px; overflow: hidden;
    background: var(--page);
    font-family: "Open Sans", Arial, sans-serif;
  }
  .canvas {
    position: relative; width: 1200px; height: 800px;
    display: flex; align-items: center; justify-content: center; gap: 40px;
  }
  .card {
    position: relative; width: 560px; height: 342px; overflow: hidden;
    background: radial-gradient(ellipse at 40% 30%, var(--ink-soft) 0%, var(--ink) 70%);
    box-shadow: 0 10px 28px rgba(0,0,0,.25);
  }
  .card__art { position: absolute; inset: 0; width: 100%; height: 100%; }
  .card__text { position: absolute; white-space: nowrap; }

  /* front */
  .front__title {
    left: 30px; top: 64px;
    font-weight: 800; font-size: 34px; letter-spacing: 1px; line-height: 1;
    color: var(--gold);
    background: linear-gradient(180deg, var(--gold-light), var(--gold) 60%, var(--gold-deep));
    -webkit-background-clip: text; background-clip: text; -webkit-text-fill-color: transparent;
  }
  .front__sub {
    left: 34px; top: 104px;
    font-weight: 700; font-size: 17px; color: var(--blue);
  }
  .front__brand {
    left: 212px; top: 150px;
    display: flex; align-items: center; gap: 9px;
  }
  .front__brand-mark { width: 20px; height: 20px; background: var(--blue); }
  .front__brand-name { font-weight: 600; font-size: 17px; color: var(--blue); letter-spacing: .5px; }
  .call { font-size: 22px; font-weight: 400; color: var(--grey); line-height: 1.2; }
  .call__number { font-weight: 700; color: var(--blue); }
  .front__call { left: 34px; bottom: 18px; }

  /* back */
  .back__offer {
    left: 0; right: 0; top: 30px; padding-left: 150px; text-align: center;
    font-weight: 800; font-size: 50px; letter-spacing: 3px; line-height: 1;
    background: linear-gradient(180deg, var(--gold-light), var(--gold) 60%, var(--gold-deep));
    -webkit-background-clip: text; background-clip: text; -webkit-text-fill-color: transparent;
  }
  .back__lines {
    left: 0; right: 0; top: 92px; padding-left: 120px; text-align: center;
    font-weight: 700; font-size: 18px; line-height: 1.3; color: var(--blue);
  }
  .back__call { left: 26px; bottom: 16px; }

  .badge {
    position: absolute; width: 118px; height: 118px; border-radius: 50%;
    background: radial-gradient(circle at 35% 30%, var(--gold-light), var(--gold) 55%, var(--gold-deep));
    display: flex; align-items: center; justify-content: center;
    box-shadow: 0 4px 10px rgba(0,0,0,.5);
  }
  .badge__face {
    width: 90px; height: 90px; border-radius: 50%;
    background: radial-gradient(circle at 40% 35%, var(--blue), var(--blue-deep));
    border: 3px solid var(--gold-light);
    display: flex; align-items: center; justify-content: center; text-align: center;
    font-weight: 800; font-size: 13px; line-height: 1.1; color: var(--gold-light);
    text-shadow: 0 1px 2px rgba(0,0,0,.5);
  }
  .badge__face--lead { font-size: 12px; }
  .badge__face--lead strong { display: block; font-size: 19px; }
  .badge--measure { left: 40px; top: 150px; }
  .badge--price { left: 222px; top: 160px; }
  .badge--family { left: 404px; top: 170px; }
</style>
</head>
<body>
<main class="canvas">

  <section class="card card--front" aria-label="Card front">
    <svg class="card__art" viewBox="0 0 560 342">
      <defs>
        <linearGradient id="goldBand" x1="0" y1="0" x2="1" y2="1">
          <stop offset="0" stop-color="#8a5a12"/>
          <stop offset=".35" stop-color="#f6da7e"/>
          <stop offset=".6" stop-color="#c8902a"/>
          <stop offset="1" stop-color="#f1cf6d"/>
        </linearGradient>
        <linearGradient id="windowTones" x1="0" y1="0" x2="0" y2="1">
          <stop offset="0" stop-color="#9a8f86"/>
          <stop offset=".5" stop-color="#5f7a4e"/>
          <stop offset="1" stop-color="#d8d2c8"/>
        </linearGradient>
        <linearGradient id="fabricTones" x1="0" y1="0" x2="1" y2="1">
          <stop offset="0" stop-color="#1f9a5a"/>
          <stop offset=".35" stop-color="#e0407a"/>
          <stop offset=".65" stop-color="#6a3fa0"/>
          <stop offset="1" stop-color="#1c3f9a"/>
        </linearGradient>
      </defs>
      <path d="M0 128 C60 158 80 244 170 246 C260 248 330 196 420 206 C480 212 530 186 560 156 L560 186 C520 222 470 236 420 232 C330 226 270 284 170 280 C80 276 40 206 0 186 Z" fill="url(#goldBand)"/>
      <rect x="386" y="6" width="166" height="194" fill="url(#goldBand)"/>
      <rect x="393" y="13" width="152" height="180" fill="url(#windowTones)" role="img" aria-label="Photo of a kitchen window fitted with a roller blind"/>
      <circle cx="140" cy="212" r="66" fill="url(#goldBand)"/>
      <circle cx="140" cy="212" r="60" fill="url(#fabricTones)" role="img" aria-label="Photo of rolled blind fabrics in many colours"/>
    </svg>
    <h1 class="card__text front__title">ROLLER BLINDS</h1>
    <p class="card__text front__sub">FREE in Home Measure &amp; Quote</p>
    <div class="card__text front__brand">
      <span class="front__brand-mark"></span>
      <span class="front__brand-name">K&amp;L INTERIORS</span>
    </div>
    <p class="card__text call front__call">Call <span class="call__number">0400 123 987</span> Today</p>
  </section>

  <section class="card card--back" aria-label="Card back">
    <svg class="card__art" viewBox="0 0 560 342" aria-hidden="true">
      <defs>
        <linearGradient id="goldBandBack" x1="0" y1="0" x2="1" y2="1">
          <stop offset="0" stop-color="#f1cf6d"/>
          <stop offset=".3" stop-color="#8a5a12"/>
          <stop offset=".55" stop-color="#f6da7e"/>
          <stop offset=".8" stop-color="#c8902a"/>
          <stop offset="1" stop-color="#f6da7e"/>
        </linearGradient>
      </defs>
      <path d="M0 20 C40 10 60 40 50 80 C40 120 70 160 150 178 C260 204 330 214 390 250 C440 278 500 282 560 280 L560 310 C490 318 420 306 370 280 C310 248 240 236 140 214 C50 194 10 150 0 110 Z" fill="url(#goldBandBack)"/>
    </svg>
    <h2 class="card__text back__offer">25% OFF</h2>
    <p class="card__text back__lines">Quality Custom Made Roller Blinds<br>Blockout – Screen – Light Filtering</p>
    <div class="badge badge--measure"><div class="badge__face badge__face--lead"><span><strong>FREE</strong>in Home Measure &amp; Quote</span></div></div>
    <div class="badge badge--price"><div class="badge__face">Best Price Guarantee</div></div>
    <div class="badge badge--family"><div class="badge__face">Family Owned &amp; Operated</div></div>
    <p class="card__text call back__call">Call <span class="call__number">0400 123 987</span> Today</p>
  </section>

</main>
</body>
</html>
```